Harbor Mortgage Relief

Please help us give our website a remake or a FACELIFT. It is not very good but it says what we need it to say. But the design is terrible.
I would like our new design font and logo to be used as the theme.

I also want more photos on the site.

I also want consistency with the pages so they look clean.

We want the professionals to do this, let's see what you got!

Thank you!
Updates

Project Deadline Extended
Reason: I can understand you want to be paid. So I will commit to the fee but I want you to have time to make a KICK ASS website for me dudes! Thanks

HI!  Just wanted to say thanks for your time on these.  A lot are great.  However the firefighters have nothing to do with Foreclosure.  We are saving peoples homes from the bank taking them and selling them.   I LOVE the house photos and the families on the website.  That is the direction we like.  THanks.

THANK U ALL FOR THE WORK!   I like a few ending in the numbers: 147  733  693  536  620  478  727  508     I will go over them and choose one soon.  Thank you.   You will be paid shortly. 

Requirements
Must have
• Bright, Upbeat photos. Color scheme should be in order. We like icons on the bottom. not just text.

```html
<!DOCTYPE html>
<html lang="en">
<head>
<meta charset="utf-8">
<title>Harbor Mortgage Relief</title>
<link href="https://fonts.googleapis.com/css2?family=Open+Sans:ital,wght@0,400;0,600;0,700;0,800;1,700;1,800&display=swap" rel="stylesheet">
<style>
:root{
  --page-bg:#ececec;
  --sheet:#ffffff;
  --brand-red:#e0202a;
  --ink:#1c1c1c;
  --nav-top:#fdeeee;
  --nav-bottom:#f6c9cb;
  --nav-divider:#d9a6a8;
  --footer:#3a3334;
  --footer-band:#4a4243;
  --footer-text:#c9c2c2;
  --phone-ink:#3a3030;
}
*{margin:0;padding:0;box-sizing:border-box}
html,body{width:1200px;height:1102px;overflow:hidden}
body{background:var(--page-bg);font-family:"Open Sans",Verdana,sans-serif;color:var(--ink)}
.sheet{position:absolute;left:85px;top:0;width:1032px;height:1102px;background:var(--sheet);box-shadow:0 0 40px rgba(0,0,0,.12)}
.brand{position:absolute;left:107px;top:28px;display:flex;align-items:center;gap:12px}
.brand-dot{width:84px;height:84px;border-radius:50%;background:var(--brand-red)}
.brand-name{font-weight:800;font-size:23px;line-height:22px;color:var(--brand-red);text-transform:uppercase;letter-spacing:.5px}
.main-nav{position:absolute;left:103px;top:128px;width:993px;height:44px;background:linear-gradient(var(--nav-top),var(--nav-bottom));display:flex}
.main-nav a{display:block;height:44px;line-height:48px;text-align:center;font-size:15px;color:#222;text-decoration:none;border-right:1px solid var(--nav-divider)}
.search{position:absolute;right:18px;top:7px;width:240px;height:30px;background:#fff;border:1px solid #d8c4c4;border-radius:4px}
.search svg{position:absolute;right:4px;top:8px}
.hero{position:absolute;left:103px;top:172px;width:993px;height:385px;
  background:
   radial-gradient(ellipse 30% 40% at 20% 95%,#f6b52a 0%,rgba(246,181,42,0) 100%),
   radial-gradient(ellipse 35% 25% at 75% 100%,#d8402a 0%,rgba(216,64,42,0) 100%),
   linear-gradient(100deg,#fffbe9 0%,#fff4d0 30%,#cfe2ef 55%,#8fb9dc 100%)}
.hero-points{position:absolute;left:90px;top:104px;list-style:none}
.hero-points li{display:flex;align-items:center;gap:10px;height:38px;font-size:23px;font-weight:800;font-style:italic;color:var(--brand-red)}
.call-bar{position:absolute;left:103px;top:557px;width:993px;height:45px;background:linear-gradient(#fdeeee,#f7cfd1);display:flex;align-items:center}
.call-label{margin-left:17px;font-size:13px;color:var(--brand-red);text-transform:uppercase}
.call-number{margin-left:21px;font-size:21px;font-weight:700;color:var(--phone-ink);letter-spacing:.5px}
.slider-dots{position:absolute;right:11px;top:11px;display:flex;gap:10px}
.slider-dots span{width:22px;height:22px;border-radius:50%;background:var(--brand-red)}
.slider-dots span.active{background:#111;box-shadow:inset 0 2px 3px #555}
.intro{position:absolute;left:119px;top:627px;width:975px;font-size:13.4px;line-height:16.7px}
.intro p{margin-bottom:16.7px}
.intro .lead{font-size:17px}
.site-footer{position:absolute;left:102px;top:958px;width:994px;height:144px;background:var(--footer)}
.footer-band{position:absolute;left:0;top:50px;width:640px;height:38px;background:linear-gradient(90deg,var(--footer-band) 70%,rgba(74,66,67,0))}
.footer-nav{position:absolute;left:28px;top:62px;display:flex;gap:0}
.footer-nav a{font-size:13px;color:var(--footer-text);text-decoration:none;margin-right:47px}
.copyright{position:absolute;left:27px;top:98px;font-size:10.5px;color:var(--footer-text)}
.footer-address{position:absolute;right:20px;top:24px;width:230px;text-align:center;font-style:normal;font-size:14px;line-height:25px;color:var(--footer-text)}
</style>
</head>
<body>
<div class="sheet"></div>

<header class="brand">
  <div class="brand-dot"></div>
  <div class="brand-name">Harbor<br>Mortgage<br>Relief</div>
</header>

<nav class="main-nav">
  <a href="#" style="width:109px">Home</a>
  <a href="#" style="width:123px">About Us</a>
  <a href="#" style="width:116px">Services</a>
  <a href="#" style="width:123px">Contact Us</a>
  <a href="#" style="width:168px">Financing Options</a>
  <div class="search">
    <svg width="20" height="20" viewBox="0 0 20 20"><circle cx="8" cy="8" r="6" fill="#f4f4f4" stroke="#666" stroke-width="1.6"/><line x1="12.5" y1="12.5" x2="18" y2="18" stroke="#444" stroke-width="3" stroke-linecap="round"/></svg>
  </div>
</nav>

<section class="hero" role="img" aria-label="Photo of a cheerful family in a sunny field of orange and yellow poppies under a blue sky">
  <ul class="hero-points">
    <li><svg width="22" height="22" viewBox="0 0 22 22"><rect x="1" y="5" width="15" height="15" fill="#fff" stroke="#555" stroke-width="2"/><path d="M5 12 l4 4 l11 -14" fill="none" stroke="#444" stroke-width="3"/></svg>NO UPFRONT FEES!</li>
    <li><svg width="22" height="22" viewBox="0 0 22 22"><rect x="1" y="5" width="15" height="15" fill="#fff" stroke="#555" stroke-width="2"/><path d="M5 12 l4 4 l11 -14" fill="none" stroke="#444" stroke-width="3"/></svg>Free Evaluation</li>
  </ul>
</section>

<div class="call-bar">
  <span class="call-label">Call toll free now</span>
  <span class="call-number">877-555-0148</span>
  <div class="slider-dots"><span></span><span class="active"></span><span></span><span></span></div>
</div>

<main class="intro">
  <p><span class="lead">S</span>pecializes in assisting homeowners who are in FORECLOSURE, by offering solid alternatives to losing your home in a Trustee Sale. Having your home foreclosed on can damage your credit for up to 7 years.&nbsp; Most foreclosures end with the home owner being evicted from their home, leaving them with no money, no place to live and without ample time to safely remove their possessions from their home. There is no need to have this happen to you.&nbsp; No matter what part of foreclosure process you are in, WE CAN HELP!</p>
  <p>If you have received a Notice of Default (NOD) or Notice of Trustee Sale (NTS), you have options.&nbsp; Contact us today to speak to one of our licensed specialist, and let us help you put this situation behind you.</p>
  <p>We speak to hundreds of homeowners every day, we understand how frustrating this can be.&nbsp; Don't live in fear of what is to come.&nbsp; You have other options, please call or email us today and we will immediately put our specialist to work finding you a solution.</p>
  <p>Don't try to handle this frustrating situation by yourself.&nbsp; HARBOR MORTGAGE RELIEF is a team of knowledgeable real estate professionals, we can offer you a better solution during this tough time.</p>
  <p>HARBOR MORTGAGE RELIEF&nbsp; has been assisting families in foreclosure for years.&nbsp; Our skill and integrity has earned us a reputation for fast, professional, courteous and thorough solutions.&nbsp; With over 50 years of real estate knowledge and experience HARBOR MORTGAGE RELIEF is ready to assist you.</p>
</main>

<footer class="site-footer">
  <div class="footer-band"></div>
  <nav class="footer-nav">
    <a href="#">Home</a><a href="#">About Us</a><a href="#">Services</a><a href="#">Contact Us</a><a href="#">Financing Options</a>
  </nav>
  <p class="copyright">Content copyright 2012. HARBORMORTGAGERELIEF.COM. All rights reserved.</p>
  <address class="footer-address">
    HARBOR MORTGAGE RELIEF<br>
    218 Bayview Avenue, Suite 300<br>
    Harborton, CA 90000<br>
    877-555-0148
  </address>
</footer>
</body>
</html>
```